Kirenu Tavern Sushi & Sake House

We need business card size flyer that will show our restaurant Logo (attached) with some sushi pictures and our address and phone number.
The flyer is specifically for 10% OFF all Alchohol beverage. Its a japanese sushi house so if you have some extra ideas to spice up the look, please advise.
Also the Address is:
418 W Marlowe Blvd
Pasadena CA 91342

Phone number: 626-555-0193

```html
<!DOCTYPE html>
<html lang="en">
<head>
<meta charset="utf-8">
<title>Kirenu Tavern Sushi &amp; Sake House – Flyer</title>
<link href="https://fonts.googleapis.com/css2?family=Barlow+Condensed:wght@400;500;700&display=swap" rel="stylesheet">
<style>
  :root {
    --page: #ffffff;
    --ink: #000000;
    --text: #ffffff;
    --promo-red: #b8393f;
    --salmon: #e0744a;
    --rice: #e9e4d8;
    --leaf: #5f8a2e;
    --tuna: #c9485a;
  }
  html, body {
    margin: 0;
    padding: 0;
    width: 995px;
    height: 1200px;
    overflow: hidden;
    background: var(--page);
    font-family: "Barlow Condensed", "Arial Narrow", sans-serif;
  }
  .canvas {
    position: relative;
    width: 995px;
    height: 1200px;
  }
  .card {
    position: absolute;
    left: 36px;
    width: 924px;
    height: 529px;
    background: var(--ink);
    overflow: hidden;
    color: var(--text);
  }
  .card--front { top: 49px; }
  .card--back { top: 627px; }
  .card-art {
    position: absolute;
    inset: 0;
    width: 924px;
    height: 529px;
  }
  .brand {
    position: absolute;
    display: flex;
    flex-direction: column;
    align-items: center;
    text-align: center;
  }
  .brand-mark {
    border: 8px solid var(--text);
    border-radius: 50%;
    box-sizing: border-box;
  }
  .brand-name {
    font-weight: 500;
    margin: 0;
    line-height: 1;
    letter-spacing: 0.5px;
  }
  .brand-tagline {
    font-weight: 500;
    margin: 0;
    line-height: 1;
  }
  .card--front .brand { left: 40px; top: 30px; width: 250px; }
  .card--front .brand-mark { width: 96px; height: 96px; margin-bottom: 12px; }
  .card--front .brand-name { font-size: 40px; }
  .card--front .brand-tagline { font-size: 18px; margin-top: 4px; }

  .card--back .brand { left: 212px; top: 140px; width: 500px; }
  .card--back .brand-mark { width: 150px; height: 150px; border-width: 12px; margin-bottom: 18px; }
  .card--back .brand-name { font-size: 64px; }
  .card--back .brand-tagline { font-size: 26px; margin-top: 8px; }

  .contact {
    position: absolute;
    right: 48px;
    top: 28px;
    padding-right: 12px;
    border-right: 3px solid var(--text);
    text-align: right;
    font-size: 27px;
    font-weight: 400;
    line-height: 33px;
    text-transform: uppercase;
  }
  .contact p { margin: 0; }
  .promo {
    position: absolute;
    right: 42px;
    top: 412px;
    text-align: right;
    text-transform: uppercase;
  }
  .promo-amount {
    margin: 0;
    font-size: 66px;
    font-weight: 700;
    line-height: 0.9;
  }
  .promo-detail {
    margin: 4px 0 0;
    font-size: 22px;
    font-weight: 500;
    line-height: 1;
  }
</style>
</head>
<body>
<main class="canvas">

  <section class="card card--front">
    <svg class="card-art" viewBox="0 0 924 529" aria-hidden="false">
      <defs>
        <linearGradient id="platterFront" x1="0" y1="0" x2="1" y2="0">
          <stop offset="0" stop-color="#6d8a3a"/>
          <stop offset="0.25" stop-color="#e0744a"/>
          <stop offset="0.5" stop-color="#c9485a"/>
          <stop offset="0.75" stop-color="#e9e4d8"/>
          <stop offset="1" stop-color="#e3a23a"/>
        </linearGradient>
        <linearGradient id="platterFade" x1="0" y1="0" x2="0" y2="1">
          <stop offset="0" stop-color="#000" stop-opacity="0.9"/>
          <stop offset="0.35" stop-color="#000" stop-opacity="0.15"/>
          <stop offset="1" stop-color="#000" stop-opacity="0"/>
        </linearGradient>
      </defs>
      <g role="img" aria-label="Photo of a sushi platter with salmon nigiri, maki rolls, tuna, cucumber garnish and greens">
        <polygon points="0,420 310,230 600,230 924,140 924,529 0,529" fill="url(#platterFront)"/>
        <polygon points="0,420 310,230 600,230 924,140 924,529 0,529" fill="url(#platterFade)"/>
      </g>
      <polygon class="promo-band" points="174,529 924,350 924,529" fill="var(--promo-red)"/>
    </svg>

    <div class="brand">
      <div class="brand-mark"></div>
      <p class="brand-name">Kirenu Tavern</p>
      <p class="brand-tagline">Extraordinary sushi and sake</p>
    </div>

    <address class="contact">
      <p>418 W Marlowe Blvd</p>
      <p>Pasadena CA 91342</p>
      <p>626-555-0193</p>
    </address>

    <div class="promo">
      <p class="promo-amount">10% OFF</p>
      <p class="promo-detail">All Alchohol Beverage</p>
    </div>
  </section>

  <section class="card card--back">
    <svg class="card-art" viewBox="0 0 924 529">
      <defs>
        <linearGradient id="platterBack" x1="0" y1="0" x2="1" y2="0">
          <stop offset="0" stop-color="#4f6a2c"/>
          <stop offset="0.3" stop-color="#a8563a"/>
          <stop offset="0.55" stop-color="#8e3a46"/>
          <stop offset="0.8" stop-color="#a9a398"/>
          <stop offset="1" stop-color="#5f7a2c"/>
        </linearGradient>
        <linearGradient id="platterBackFade" x1="0" y1="0" x2="0" y2="1">
          <stop offset="0" stop-color="#000" stop-opacity="1"/>
          <stop offset="0.4" stop-color="#000" stop-opacity="0.35"/>
          <stop offset="1" stop-color="#000" stop-opacity="0.2"/>
        </linearGradient>
      </defs>
      <g role="img" aria-label="Dimmed photo of a sushi platter filling the lower part of the card">
        <rect x="0" y="150" width="924" height="379" fill="url(#platterBack)"/>
        <rect x="0" y="150" width="924" height="379" fill="url(#platterBackFade)"/>
      </g>
    </svg>

    <div class="brand">
      <div class="brand-mark"></div>
      <p class="brand-name">Kirenu Tavern</p>
      <p class="brand-tagline">Extraordinary sushi and sake</p>
    </div>
  </section>

</main>
</body>
</html>
```